WTF!!! We need a modern professional website for a business litigation law firm.

We need a modern, clean, professional and uncomplicated website for a new business trial and litigation law firm called "Hallorand Trial Firm PLLC". Website must be mobile optimized for iPad and smartphone. The law firm specializes in counseling and representing large corporations, small businesses and entrepreneurs in and out of the courtroom. Lawyers in the firm serve as Florida counsel and trial counsel to organizations facing claims involving product liability, premises liability, professional liability, vehicle and transportation liability, warranty claims, construction defects and delay claims, complex business disputes, commercial litigation and bid disputes in State and Federal Courts. The website is mainly to provide information about the firm, and should include sections describing the firm, identifying the Industries Served and Areas of Practice ," a separate page identifying the "Professionals", a separate page for "Resources & Advisories," and a traveling "Connect With Us" button a site visitor can click on that will launch an email to the Firm's general email account. The website should allow us to easily modify the content on these pages, and let us add/modify links to external information sources. We will not sell anything or take payments through the website. We do need to be able to easily upload and update photographs of attorneys and add new attorneys names/email hyperlinks as the firm grows. We would like to add developments in the law or success stories easily and quickly, such as through a blog page. On the "Connect With Us" page the website should have hyperlinks to email the Firm, and there should be hyperlinks to email each professional on the "Professionals" page. The website should be viewable on mobile devices without distortion. The law firm focuses on trial work and should have some imagery associated with courtrooms, but the overall theme of the site should be modern, clean, and communicate sophistication and strength. The website should be made in Wordpress. We have uploaded logo files for Hallorand Trial Firm.

Target Market(s)

Corporations and companies that are looking for legal representation. Other attorneys/legal industry.

Industry/Entity Type

Legal Industry

Coding

Coded - Design and coding required

Number of Pages Required

1 page

Font styles to use
Sans Serif

Requirements
Must have
• Simple, clean, sophisticated, modern website that includes the logo, watermark of logo, and the elements described above.
Nice to have
• Pictures of city scape, buildings, courtroom, team members.

```html
<!DOCTYPE html>
<html lang="en">
<head>
<meta charset="utf-8">
<title>Hallorand Trial Firm</title>
<link href="https://fonts.googleapis.com/css2?family=League+Spartan:wght@400;500;600;700&display=swap" rel="stylesheet">
<style>
:root{
  --navy:#243249;
  --gold:#d4963a;
  --ink:#2a2f3a;
  --text:#3c4150;
  --muted:#6b6f78;
  --mist:#f0eff0;
  --line:#e1e1e4;
  --footer:#1f1f20;
  --white:#ffffff;
}
*{box-sizing:border-box;margin:0;padding:0}
html,body{width:1200px;height:4448px;overflow:hidden}
body{font-family:"League Spartan",Arial,sans-serif;color:var(--text);background:var(--white);position:relative}
.abs{position:absolute}
section,header,footer{position:absolute;left:0;width:1200px}
.gold{color:var(--gold)}
.navy{color:var(--navy)}
.title{position:absolute;left:0;width:1200px;text-align:center;font-size:31px;font-weight:600;color:var(--navy);letter-spacing:-0.3px;line-height:36px}
.title span{color:var(--gold)}

/* buttons */
.btn{position:absolute;display:flex;text-decoration:none}
.btn-ico{background:var(--navy);display:flex;align-items:center;justify-content:center}
.btn-label{background:var(--gold);color:var(--white);display:flex;align-items:center;padding:0 16px;font-size:13px;font-weight:500;letter-spacing:.3px;text-transform:uppercase;flex:1}
.btn-outline .btn-label{background:var(--white);color:var(--navy);border:1px solid var(--gold);font-size:10.5px;padding:0 10px}

/* header */
.site-header{top:0;height:107px;background:var(--white)}
.brand{position:absolute;left:109px;top:30px;width:120px;text-align:center;font-weight:700;color:var(--ink);font-size:19px;line-height:20px;letter-spacing:.3px}
.brand small{display:block;font-size:9px;letter-spacing:2px;line-height:12px}
.phone-box{position:absolute;left:932px;top:21px;width:156px;height:33px;border:1px solid #cfd0d4;display:flex}
.phone-box .ico{width:33px;background:var(--navy);display:flex;align-items:center;justify-content:center}
.phone-box .num{flex:1;display:flex;align-items:center;justify-content:center;font-size:11px;color:var(--text)}
.main-nav{position:absolute;top:77px;left:0;height:16px}
.main-nav a{position:absolute;font-size:11.5px;text-transform:uppercase;color:#5b606a;text-decoration:none;white-space:nowrap;letter-spacing:.2px}
.main-nav a.active{color:var(--navy);font-weight:500}

/* hero */
.hero{top:107px;height:458px}
.hero-media{position:absolute;inset:0;background:linear-gradient(100deg,#f4f1ec 0%,#ece6dc 32%,#c9b9a3 52%,#8a6a52 70%,#5a4036 86%,#3d3431 100%)}
.hero h1{position:absolute;left:109px;top:72px;font-size:26px;line-height:43px;font-weight:600;color:var(--navy);letter-spacing:-0.3px}
.hero p{position:absolute;left:110px;top:160px;width:470px;font-size:14px;line-height:36px;color:var(--ink)}

/* industries */
.industries{top:565px;height:1089px}
.ind-panel{position:absolute;left:110px;top:174px;width:322px;height:451px;background:var(--navy);box-shadow:0 6px 14px rgba(0,0,0,.18)}
.ind-item{position:absolute;left:0;width:322px;height:40px;display:flex;align-items:center;color:var(--white);font-size:17px;letter-spacing:.3px}
.ind-item svg{position:absolute;left:74px}
.ind-item span{position:absolute;left:130px}
.ind-active{position:absolute;left:35px;top:273px;width:254px;height:50px;background:var(--gold);clip-path:polygon(18px 0,100% 0,calc(100% - 18px) 100%,0 100%)}
.sit-icon{position:absolute;left:514px;top:176px}
.sit-title{position:absolute;left:511px;top:278px;font-size:31px;font-weight:600;color:var(--gold)}
.sit-copy{position:absolute;left:513px;width:580px;font-size:14px;line-height:34.5px;color:var(--text)}
.city-band{position:absolute;left:0;top:747px;width:1200px;height:342px;background:linear-gradient(180deg,#ffffff 0%,#e9e9ea 22%,#a9abae 55%,#5f6266 85%,#4b4d50 100%)}

/* about */
.about{top:1654px;height:731px;background:var(--mist)}
.about-lead{position:absolute;left:170px;top:140px;width:860px;text-align:center;font-size:14px;line-height:34.5px;color:var(--text)}
.team-photo{position:absolute;left:110px;top:297px;width:405px;height:356px;background:linear-gradient(160deg,#c6cdd4 0%,#8e98a3 40%,#5c6670 75%,#3e454c 100%)}
.about-card{position:absolute;left:515px;top:316px;width:573px;height:325px;background:var(--white)}
.about-card h3{position:absolute;left:48px;top:22px;width:480px;font-size:16px;line-height:38px;font-weight:500;color:var(--ink);text-transform:uppercase;letter-spacing:.2px}
.about-card p{position:absolute;left:48px;top:106px;width:490px;font-size:14px;line-height:34.5px}

/* practice */
.practice{top:2385px;height:493px}
.area-card{position:absolute;top:157px;width:185px;height:171px;background:var(--white);border:1px solid var(--line);box-shadow:0 2px 6px rgba(0,0,0,.08);text-align:center}
.area-card svg{position:absolute;left:62px;top:30px}
.area-card .label{position:absolute;left:0;width:100%;font-size:14px;line-height:30px;color:var(--ink);text-transform:uppercase}

/* success */
.stories{top:2878px;height:449px;background:var(--mist)}
.story{position:absolute;top:128px;height:252px;background:var(--white);border-bottom:5px solid var(--gold);box-shadow:0 2px 8px rgba(0,0,0,.05)}
.story .quote{position:absolute;left:34px;top:24px;font-size:46px;line-height:46px;color:var(--gold);font-weight:700}
.story p{position:absolute;left:34px;top:64px;width:425px;font-size:13px;line-height:29.5px;color:var(--ink)}
.story .avatar{position:absolute;left:35px;top:170px;width:54px;height:54px;border-radius:50%;background:linear-gradient(160deg,#cfc7bf,#6f625a)}
.story .name{position:absolute;left:117px;top:174px;font-size:13.5px;color:var(--navy);font-weight:500;letter-spacing:.3px}
.story .stars{color:var(--gold);font-size:12px;margin-left:12px;letter-spacing:2px}
.story .role{position:absolute;left:117px;top:200px;font-size:11px;color:var(--muted)}
.arrow{position:absolute;top:243px}

/* news */
.news{top:3327px;height:755px}
.post{position:absolute;top:159px;width:270px;height:420px;border-right:2px solid var(--line)}
.post-media{width:268px;height:168px;background:linear-gradient(150deg,#c9c4bd 0%,#8d8580 45%,#4b4d55 100%)}
.post .date{position:absolute;left:0;top:195px;font-size:13.5px;color:var(--gold)}
.post h4{position:absolute;left:0;top:233px;font-size:13.5px;font-weight:500;color:var(--ink);text-transform:uppercase}
.post p{position:absolute;left:0;top:263px;width:250px;font-size:12.5px;line-height:27.7px;color:var(--text)}

/* footer */
.site-footer{top:4082px;height:366px;background:var(--footer);color:#e6e6e6}
.foot-brand{position:absolute;left:109px;top:100px;width:195px;text-align:center;font-size:32px;font-weight:700;color:var(--white);letter-spacing:.5px;line-height:34px}
.foot-brand small{display:block;font-size:15px;letter-spacing:4px;line-height:20px;font-weight:700}
.foot-head{position:absolute;top:52px;font-size:20px;color:var(--gold);font-weight:500;letter-spacing:.3px}
.foot-link{position:absolute;font-size:13.5px;color:#e6e6e6}
.c-ico{position:absolute;left:890px;width:38px;height:38px;border-radius:50%;background:#333335;display:flex;align-items:center;justify-content:center}
.c-text{position:absolute;left:950px;font-size:13.5px;line-height:26px;color:#e6e6e6}
.copyright{position:absolute;left:0;top:325px;width:1200px;text-align:center;font-size:12px;color:#e6e6e6;letter-spacing:.3px}
</style>
</head>
<body>

<header class="site-header">
  <div class="brand">HALLORAND<small>TRIAL FIRM</small></div>
  <div class="phone-box">
    <div class="ico"><svg width="12" height="12" viewBox="0 0 24 24"><path fill="#fff" d="M6.6 10.8a15 15 0 0 0 6.6 6.6l2.2-2.2a1 1 0 0 1 1-.25 11.4 11.4 0 0 0 3.6.57 1 1 0 0 1 1 1V20a1 1 0 0 1-1 1A17 17 0 0 1 3 4a1 1 0 0 1 1-1h3.5a1 1 0 0 1 1 1c0 1.25.2 2.45.57 3.6a1 1 0 0 1-.25 1z"/></svg></div>
    <div class="num">+1 888 888 8888</div>
  </div>
  <nav class="main-nav">
    <a class="active" style="left:368px">Home</a>
    <a style="left:433px">About</a>
    <a style="left:504px">Practice Areas</a>
    <a style="left:642px">Professionals</a>
    <a style="left:773px">Blog</a>
    <a style="left:836px">Resources &amp; Advisories</a>
    <a style="left:1029px">Contact</a>
  </nav>
</header>

<section class="hero">
  <div class="hero-media" role="img" aria-label="Two professional women reviewing legal documents at an office desk"></div>
  <h1><span class="gold">PROVIDING TRUSTED</span> LEGAL COUNSEL<br>&amp; UNMATCHED TRIAL REPRESENTATION</h1>
  <p>Lorem ipsum dolor sit amet, consectetur adipiscing elit, sed do eiusmod tempor incididunt ut</p>
  <a class="btn" style="left:110px;top:252px;width:177px;height:30px">
    <span class="btn-ico" style="width:32px"><svg width="11" height="11" viewBox="0 0 24 24"><path fill="#fff" d="M6.6 10.8a15 15 0 0 0 6.6 6.6l2.2-2.2a1 1 0 0 1 1-.25 11.4 11.4 0 0 0 3.6.57 1 1 0 0 1 1 1V20a1 1 0 0 1-1 1A17 17 0 0 1 3 4a1 1 0 0 1 1-1h3.5a1 1 0 0 1 1 1c0 1.25.2 2.45.57 3.6a1 1 0 0 1-.25 1z"/></svg></span>
    <span class="btn-label" style="font-size:11px;padding:0 12px">Connect With Us</span>
  </a>
</section>

<section class="industries">
  <h2 class="title" style="top:75px"><span>INDUSTRIES</span> WE SERVE</h2>

  <div class="ind-panel">
    <div class="ind-active"></div>
    <div class="ind-item" style="top:56px">
      <svg width="34" height="34" viewBox="0 0 34 34" fill="none" stroke="#fff" stroke-width="1.6"><rect x="6" y="5" width="18" height="24" rx="2"/><path d="M11 12h8M11 17h8M11 22h5"/><circle cx="25" cy="24" r="5"/></svg>
      <span>LOREM IPSUM</span>
    </div>
    <div class="ind-item" style="top:130px">
      <svg width="34" height="34" viewBox="0 0 34 34" fill="none" stroke="#fff" stroke-width="1.6"><rect x="7" y="4" width="18" height="25" rx="2"/><path d="M12 11h8M12 16h8M12 21h6"/><path d="M24 21l4 4-4 4"/></svg>
      <span>LOREM IPSUM</span>
    </div>
    <div class="ind-item" style="top:204px">
      <svg width="34" height="34" viewBox="0 0 34 34" fill="none" stroke="#fff" stroke-width="1.6"><path d="M4 15a13 11 0 0 1 26 0z"/><path d="M17 15v6"/><circle cx="11" cy="24" r="2"/><circle cx="17" cy="24" r="2"/><circle cx="23" cy="24" r="2"/><path d="M8 31a3 3 0 0 1 6 0M14 31a3 3 0 0 1 6 0M20 31a3 3 0 0 1 6 0"/></svg>
      <span>LOREM IPSUM</span>
    </div>
    <div class="ind-item" style="top:278px">
      <svg width="34" height="34" viewBox="0 0 34 34" fill="none" stroke="#fff" stroke-width="1.6"><rect x="6" y="5" width="18" height="24" rx="2"/><path d="M11 12h8M11 17h8"/><path d="M25 19l5 2v4c0 3-2 5-5 6-3-1-5-3-5-6v-4z"/></svg>
      <span>LOREM IPSUM</span>
    </div>
    <div class="ind-item" style="top:352px">
      <svg width="34" height="34" viewBox="0 0 34 34" fill="none" stroke="#fff" stroke-width="1.6"><rect x="8" y="4" width="18" height="25" rx="2"/><circle cx="17" cy="12" r="3"/><path d="M12 21a5 5 0 0 1 10 0"/><path d="M4 24h6v6H4z"/></svg>
      <span>LOREM IPSUM</span>
    </div>
  </div>

  <svg class="sit-icon" width="84" height="84" viewBox="0 0 84 84">
    <rect x="17" y="17" width="50" height="50" transform="rotate(45 42 42)" fill="#dca04a" stroke="#c8852a" stroke-width="2"/>
    <rect x="33" y="28" width="16" height="22" rx="1.5" fill="none" stroke="#fff" stroke-width="1.6"/>
    <path d="M37 35h8M37 40h8" stroke="#fff" stroke-width="1.6"/>
    <path d="M49 42l6 2v4c0 3-3 5-6 6-3-1-6-3-6-6v-4z" fill="#dca04a" stroke="#fff" stroke-width="1.6"/>
  </svg>
  <h3 class="sit-title">SITUATION 1</h3>
  <p class="sit-copy" style="top:332px">Lorem ipsum dolor sit amet, consectetur adipiscing elit, sed do eiusmod tempor incididunt ut labore et dolore magna aliqua. Ut enim ad minim veniam, quis nostrud exercitation ullamco laboris nisi ut aliquip ex ea commodo consequat. Duis aute irure dolor in reprehenderit in voluptate velit esse cillum dolore eu fugiat nulla pariatur sint occaecat cupidatat non proident, sunt in culpa qui officia deserunt mollit anim id est laborum.</p>
  <p class="sit-copy" style="top:551px">Lorem ipsum dolor sit amet, consectetur adipiscing elit, sed do eiusmod tempor incididunt ut labore et dolore magna aliqua. Ut enim ad minim veniam, quis nostrud exercitation ullamco laboris nisi ut aliquip ex ea commodo consequat.</p>
  <a class="btn" style="left:513px;top:718px;width:174px;height:38px">
    <span class="btn-ico" style="width:40px"><svg width="13" height="13" viewBox="0 0 24 24"><path fill="#fff" d="M6.6 10.8a15 15 0 0 0 6.6 6.6l2.2-2.2a1 1 0 0 1 1-.25 11.4 11.4 0 0 0 3.6.57 1 1 0 0 1 1 1V20a1 1 0 0 1-1 1A17 17 0 0 1 3 4a1 1 0 0 1 1-1h3.5a1 1 0 0 1 1 1c0 1.25.2 2.45.57 3.6a1 1 0 0 1-.25 1z"/></svg></span>
    <span class="btn-label">Contact Us</span>
  </a>

  <div class="city-band" role="img" aria-label="Grey city skyline with a person holding an umbrella, fading into white"></div>
</section>

<section class="about">
  <h2 class="title" style="top:79px"><span>ABOUT</span> HALLORAND TRIAL FIRM</h2>
  <p class="about-lead">Lorem ipsum dolor sit amet, consectetur adipiscing elit, sed do eiusmod tempor incididunt ut labore et dolore magna aliqua. Ut enim ad minim veniam, quis nostrud exercitation ullamco laboris nisi ut aliquip ex ea commodo aute irure dolor in reprehenderit in voluptate velit esse cillum dolore eu.</p>
  <div class="team-photo" role="img" aria-label="Smiling team of firm professionals standing together in an office"></div>
  <div class="about-card">
    <h3>Lorem ipsum dolor sit amet, consectetur adipiscing elit sed do eiusmod</h3>
    <p>Lorem ipsum dolor sit amet, consectetur adipiscing elit, sed do eiusmod tempor incididunt ut labore et dolore magna aliqua enim ad minim veniam.</p>
    <a class="btn" style="left:48px;top:250px;width:162px;height:37px">
      <span class="btn-ico" style="width:38px"><svg width="13" height="13" viewBox="0 0 24 24"><path fill="#fff" d="M6.6 10.8a15 15 0 0 0 6.6 6.6l2.2-2.2a1 1 0 0 1 1-.25 11.4 11.4 0 0 0 3.6.57 1 1 0 0 1 1 1V20a1 1 0 0 1-1 1A17 17 0 0 1 3 4a1 1 0 0 1 1-1h3.5a1 1 0 0 1 1 1c0 1.25.2 2.45.57 3.6a1 1 0 0 1-.25 1z"/></svg></span>
      <span class="btn-label">Learn More</span>
    </a>
  </div>
</section>

<section class="practice">
  <h2 class="title" style="top:76px"><span>AREAS OF</span> PRACTICE</h2>

  <div class="area-card" style="left:110px">
    <svg width="60" height="60" viewBox="0 0 60 60" fill="none" stroke="#2a2f3a" stroke-width="1.6"><path d="M8 18l18-9 18 9-18 9z"/><path d="M8 18v22l18 9V27M44 18v10"/><path d="M46 32l8 3v6c0 5-4 8-8 9-4-1-8-4-8-9v-6z" stroke="#d4963a"/><path d="M42 41l3 3 5-6" stroke="#d4963a"/></svg>
    <div class="label" style="top:119px">Product Liability</div>
  </div>
  <div class="area-card" style="left:308px">
    <svg width="60" height="60" viewBox="0 0 60 60" fill="none" stroke="#2a2f3a" stroke-width="1.6"><rect x="14" y="6" width="32" height="46"/><path d="M6 52h48"/><path d="M20 13h4M28 13h4M36 13h4M20 21h4M28 21h4M36 21h4M20 29h4M28 29h4M36 29h4M20 37h4M36 37h4" stroke="#d4963a"/><rect x="26" y="40" width="8" height="12"/></svg>
    <div class="label" style="top:119px">Premises Liability</div>
  </div>
  <div class="area-card" style="left:507px">
    <svg width="60" height="60" viewBox="0 0 60 60" fill="none" stroke="#2a2f3a" stroke-width="1.6"><circle cx="26" cy="14" r="8"/><path d="M10 44c0-10 7-17 16-17s16 7 16 17z"/><circle cx="44" cy="40" r="8" stroke="#d4963a"/><path d="M40 40l3 3 5-5" stroke="#d4963a"/></svg>
    <div class="label" style="top:104px">Professional<br>Liability</div>
  </div>
  <div class="area-card" style="left:705px">
    <svg width="60" height="60" viewBox="0 0 60 60" fill="none" stroke="#2a2f3a" stroke-width="1.6"><path d="M10 6h26l8 8v40H10z"/><path d="M16 18h20M16 24h20M16 30h14M16 36h14M16 42h12"/><path d="M44 30l9 3v7c0 6-4 9-9 11-5-2-9-5-9-11v-7z" stroke="#d4963a"/><path d="M40 40l3 3 5-6" stroke="#d4963a"/></svg>
    <div class="label" style="top:119px">Warranty Claims</div>
  </div>
  <div class="area-card" style="left:903px">
    <svg width="60" height="60" viewBox="0 0 60 60" fill="none" stroke="#2a2f3a" stroke-width="1.6"><path d="M6 18L30 6l24 12z"/><path d="M8 22h44M8 48h44M5 53h50"/><path d="M13 26v18M21 26v18M39 26v18M47 26v18"/><rect x="26" y="28" width="8" height="16" stroke="#d4963a"/></svg>
    <div class="label" style="top:119px">Federal Courts</div>
  </div>

  <a class="btn" style="left:520px;top:374px;width:162px;height:35px">
    <span class="btn-ico" style="width:38px"><svg width="13" height="13" viewBox="0 0 24 24"><path fill="#fff" d="M6.6 10.8a15 15 0 0 0 6.6 6.6l2.2-2.2a1 1 0 0 1 1-.25 11.4 11.4 0 0 0 3.6.57 1 1 0 0 1 1 1V20a1 1 0 0 1-1 1A17 17 0 0 1 3 4a1 1 0 0 1 1-1h3.5a1 1 0 0 1 1 1c0 1.25.2 2.45.57 3.6a1 1 0 0 1-.25 1z"/></svg></span>
    <span class="btn-label">View More</span>
  </a>
</section>

<section class="stories">
  <h2 class="title" style="top:46px"><span>SUCCESS</span> STORIES</h2>
  <svg class="arrow" style="left:48px" width="14" height="22" viewBox="0 0 14 22"><path d="M11 2L3 11l8 9" fill="none" stroke="#2a2f3a" stroke-width="2"/></svg>
  <svg class="arrow" style="left:1137px" width="14" height="22" viewBox="0 0 14 22"><path d="M3 2l8 9-8 9" fill="none" stroke="#2a2f3a" stroke-width="2"/></svg>

  <div class="story" style="left:126px;width:473px">
    <div class="quote">&ldquo;</div>
    <p>Lorem ipsum dolor sit amet, consectetur adipiscing elit, sed do eiusmod tempor incididunt ut labore et dolore magna aliqua enim ad minim veniam consequat.</p>
    <div class="avatar" role="img" aria-label="Portrait of client"></div>
    <div class="name">MARCUS ELLERY<span class="stars">★★★★★</span></div>
    <div class="role">CEO</div>
  </div>
  <div class="story" style="left:616px;width:472px">
    <div class="quote">&ldquo;</div>
    <p>Lorem ipsum dolor sit amet, consectetur adipiscing elit, sed do eiusmod tempor incididunt ut labore et dolore magna aliqua enim ad minim veniam consequat.</p>
    <div class="avatar" role="img" aria-label="Portrait of client"></div>
    <div class="name">LINA HADDAD<span class="stars">★★★★★</span></div>
    <div class="role">GENERAL MANAGER</div>
  </div>
</section>

<section class="news">
  <h2 class="title" style="top:75px"><span>LATEST</span> NEWS</h2>

  <article class="post" style="left:155px">
    <div class="post-media" role="img" aria-label="Business team meeting around a table with laptops"></div>
    <div class="date">13 MAY 2024</div>
    <h4>Lorem ipsum dolor sit amet</h4>
    <p>Lorem ipsum dolor sit amet, consectetur adipiscing elit, sed do eiusmod tempor incididunt ut labore et dolore magna aliqua.</p>
    <a class="btn btn-outline" style="left:0;top:376px;width:125px;height:27px">
      <span class="btn-ico" style="width:27px"><svg width="10" height="10" viewBox="0 0 24 24"><path fill="#fff" d="M6.6 10.8a15 15 0 0 0 6.6 6.6l2.2-2.2a1 1 0 0 1 1-.25 11.4 11.4 0 0 0 3.6.57 1 1 0 0 1 1 1V20a1 1 0 0 1-1 1A17 17 0 0 1 3 4a1 1 0 0 1 1-1h3.5a1 1 0 0 1 1 1c0 1.25.2 2.45.57 3.6a1 1 0 0 1-.25 1z"/></svg></span>
      <span class="btn-label">Learn More</span>
    </a>
  </article>
  <article class="post" style="left:464px">
    <div class="post-media" role="img" aria-label="Attorney signing documents with a client at a desk"></div>
    <div class="date">18 AUGUST 2024</div>
    <h4>Lorem ipsum dolor sit amet</h4>
    <p>Lorem ipsum dolor sit amet, consectetur adipiscing elit, sed do eiusmod tempor incididunt ut labore et dolore magna aliqua.</p>
    <a class="btn btn-outline" style="left:0;top:376px;width:125px;height:27px">
      <span class="btn-ico" style="width:27px"><svg width="10" height="10" viewBox="0 0 24 24"><path fill="#fff" d="M6.6 10.8a15 15 0 0 0 6.6 6.6l2.2-2.2a1 1 0 0 1 1-.25 11.4 11.4 0 0 0 3.6.57 1 1 0 0 1 1 1V20a1 1 0 0 1-1 1A17 17 0 0 1 3 4a1 1 0 0 1 1-1h3.5a1 1 0 0 1 1 1c0 1.25.2 2.45.57 3.6a1 1 0 0 1-.25 1z"/></svg></span>
      <span class="btn-label">Learn More</span>
    </a>
  </article>
  <article class="post" style="left:773px">
    <div class="post-media" role="img" aria-label="Two lawyers discussing paperwork in an office"></div>
    <div class="date">22 JUNE 2024</div>
    <h4>Lorem ipsum dolor sit amet</h4>
    <p>Lorem ipsum dolor sit amet, consectetur adipiscing elit, sed do eiusmod tempor incididunt ut labore et dolore magna aliqua.</p>
    <a class="btn btn-outline" style="left:0;top:376px;width:125px;height:27px">
      <span class="btn-ico" style="width:27px"><svg width="10" height="10" viewBox="0 0 24 24"><path fill="#fff" d="M6.6 10.8a15 15 0 0 0 6.6 6.6l2.2-2.2a1 1 0 0 1 1-.25 11.4 11.4 0 0 0 3.6.57 1 1 0 0 1 1 1V20a1 1 0 0 1-1 1A17 17 0 0 1 3 4a1 1 0 0 1 1-1h3.5a1 1 0 0 1 1 1c0 1.25.2 2.45.57 3.6a1 1 0 0 1-.25 1z"/></svg></span>
      <span class="btn-label">Learn More</span>
    </a>
  </article>

  <a class="btn" style="left:496px;top:635px;width:207px;height:35px">
    <span class="btn-ico" style="width:38px"><svg width="13" height="13" viewBox="0 0 24 24"><path fill="#fff" d="M6.6 10.8a15 15 0 0 0 6.6 6.6l2.2-2.2a1 1 0 0 1 1-.25 11.4 11.4 0 0 0 3.6.57 1 1 0 0 1 1 1V20a1 1 0 0 1-1 1A17 17 0 0 1 3 4a1 1 0 0 1 1-1h3.5a1 1 0 0 1 1 1c0 1.25.2 2.45.57 3.6a1 1 0 0 1-.25 1z"/></svg></span>
    <span class="btn-label">View More Blogs</span>
  </a>
</section>

<footer class="site-footer">
  <div class="foot-brand">HALLORAND<small>TRIAL FIRM</small></div>

  <div class="foot-head" style="left:444px">QUICK LINKS</div>
  <div class="foot-link" style="left:444px;top:117px">Home</div>
  <div class="foot-link" style="left:444px;top:153px">About</div>
  <div class="foot-link" style="left:444px;top:190px">Practice Areas</div>
  <div class="foot-link" style="left:444px;top:227px">Professionals</div>
  <div class="foot-link" style="left:639px;top:117px">Blog</div>
  <div class="foot-link" style="left:639px;top:153px">Resources &amp; Advisories</div>
  <div class="foot-link" style="left:639px;top:190px">Contact</div>

  <div class="foot-head" style="left:889px">CONTACT US</div>
  <div class="c-ico" style="top:105px"><svg width="14" height="14" viewBox="0 0 24 24"><path fill="#fff" d="M6.6 10.8a15 15 0 0 0 6.6 6.6l2.2-2.2a1 1 0 0 1 1-.25 11.4 11.4 0 0 0 3.6.57 1 1 0 0 1 1 1V20a1 1 0 0 1-1 1A17 17 0 0 1 3 4a1 1 0 0 1 1-1h3.5a1 1 0 0 1 1 1c0 1.25.2 2.45.57 3.6a1 1 0 0 1-.25 1z"/></svg></div>
  <div class="c-text" style="top:111px">+1 888 888 8888</div>
  <div class="c-ico" style="top:160px"><svg width="16" height="12" viewBox="0 0 16 12"><rect x="0.5" y="0.5" width="15" height="11" fill="#fff"/><path d="M1 1l7 6 7-6" fill="none" stroke="#333335" stroke-width="1.2"/></svg></div>
  <div class="c-text" style="top:166px">contact@hallorandfirm.example</div>
  <div class="c-ico" style="top:219px"><svg width="14" height="18" viewBox="0 0 14 18"><path d="M7 0a6 6 0 0 1 6 6c0 4-6 10-6 10S1 10 1 6a6 6 0 0 1 6-6z" fill="#fff"/><circle cx="7" cy="6" r="2.2" fill="#333335"/></svg></div>
  <div class="c-text" style="top:200px">23, Hallorand Lorem<br>897 784</div>

  <div class="copyright">© HALLORAND TRAIL FIRM 2025 &nbsp;|&nbsp; ALL RIGHTS RESERVED</div>
</footer>

</body>
</html>
```